Online Psychology Practice needs business cards.

Online Psychology service needs business cards. Have own logo- please see uploaded. I have other file formats if you need (not sure one needed?)

Details for Business Card:
Fiona Kettlewood
Clinical Psychologist BPsych, BPsych (Hons), MPsych (Clin), MAPS
T: 0457260714 | F: 08 71526804
E: hello@harbourlightmindcarestudio.com.au
W: harbourlightmindcarestudio.com.au

Industry/Entity Type

Health

Contact Information for Business Card

Logo plus details above (couldn't write in this section)

```html
<!DOCTYPE html>
<html lang="en">
<head>
<meta charset="utf-8">
<title>Harbourlight Mindcare Studio – Business Cards</title>
<link rel="stylesheet" href="https://fonts.googleapis.com/css2?family=Open+Sans:wght@400;700&display=swap">
<style>
  :root {
    --ink-blue: #1b5e86;
    --deep-blue: #185a80;
    --text-dark: #1a1a1a;
    --card-white: #ffffff;
    --backdrop: #e6e8ea;
    --shadow: rgba(0, 0, 0, 0.18);
  }
  * { margin: 0; padding: 0; box-sizing: border-box; }
  html, body {
    width: 1200px;
    height: 1200px;
    overflow: hidden;
    background: var(--backdrop);
    font-family: "Open Sans", Arial, sans-serif;
  }
  .stage {
    position: relative;
    width: 1200px;
    height: 1200px;
    display: flex;
    align-items: center;
    justify-content: center;
    gap: 60px;
  }
  .card {
    position: relative;
    width: 420px;
    height: 670px;
    border-radius: 30px;
    overflow: hidden;
    box-shadow: 0 14px 34px var(--shadow);
  }
  /* Front */
  .card--front {
    background: var(--card-white);
    display: flex;
    flex-direction: column;
    align-items: center;
    text-align: center;
  }
  .brand {
    margin-top: 120px;
    display: flex;
    flex-direction: column;
    align-items: center;
    gap: 18px;
  }
  .brand-dot {
    width: 74px;
    height: 74px;
    border-radius: 50%;
    background: var(--ink-blue);
  }
  .brand-name {
    font-weight: 700;
    font-size: 30px;
    line-height: 1.15;
    letter-spacing: 0.5px;
    color: var(--ink-blue);
  }
  .card--back .brand-dot { background: var(--card-white); }
  .card--back .brand-name { color: var(--card-white); }
  .person {
    margin-top: 48px;
  }
  .person-name {
    font-weight: 700;
    font-size: 30px;
    color: var(--ink-blue);
    line-height: 1.1;
  }
  .person-role {
    margin-top: 6px;
    font-size: 16px;
    line-height: 1.3;
    color: var(--text-dark);
  }
  .divider {
    margin-top: 34px;
    width: 56px;
    height: 3px;
    background: var(--ink-blue);
  }
  .contact-icons {
    margin-top: 40px;
    display: flex;
    gap: 5px;
  }
  .contact-icons svg { width: 16px; height: 16px; }
  .contacts {
    margin-top: 6px;
    list-style: none;
    font-size: 14.5px;
    line-height: 1.4;
    color: var(--text-dark);
  }
  .footer-band {
    position: absolute;
    left: 0; right: 0; bottom: 0;
    height: 34px;
    background: var(--ink-blue);
  }
  /* Back */
  .card--back {
    background: var(--deep-blue);
    display: flex;
    align-items: center;
    justify-content: center;
  }
  .card--back .brand { margin-top: 0; }
</style>
</head>
<body>
<main class="stage">
  <section class="card card--front" aria-label="Business card front">
    <div class="brand">
      <span class="brand-dot"></span>
      <p class="brand-name">Harbourlight<br>Mindcare Studio</p>
    </div>
    <div class="person">
      <h1 class="person-name">Fiona Kettlewood</h1>
      <p class="person-role">Clinical Psychologist BPsych,<br>BPsych (Hons), MPsych (Clin), MAPS</p>
    </div>
    <div class="divider"></div>
    <div class="contact-icons" aria-hidden="true">
      <svg viewBox="0 0 16 16"><circle cx="8" cy="8" r="7" fill="none" stroke="#1b5e86" stroke-width="1.3"/><path d="M5.3 4.5l1.4 1.6-.7 1c.6 1.1 1.3 1.8 2.4 2.4l1-.7 1.6 1.4-.9 1.2C7.7 11.3 4.7 8.3 4.1 5.4z" fill="#1b5e86"/></svg>
      <svg viewBox="0 0 16 16"><circle cx="8" cy="8" r="7" fill="none" stroke="#1b5e86" stroke-width="1.3"/><rect x="4.5" y="6.5" width="7" height="4" fill="#1b5e86"/><rect x="5.5" y="4" width="5" height="2.5" fill="none" stroke="#1b5e86"/></svg>
      <svg viewBox="0 0 16 16"><circle cx="8" cy="8" r="7" fill="none" stroke="#1b5e86" stroke-width="1.3"/><rect x="4.3" y="5.3" width="7.4" height="5.4" fill="none" stroke="#1b5e86"/><path d="M4.3 5.3L8 8.4l3.7-3.1" fill="none" stroke="#1b5e86"/></svg>
      <svg viewBox="0 0 16 16"><circle cx="8" cy="8" r="7" fill="none" stroke="#1b5e86" stroke-width="1.3"/><circle cx="8" cy="8" r="3.8" fill="none" stroke="#1b5e86"/><path d="M4.2 8h7.6M8 4.2c-1.6 2.3-1.6 5.3 0 7.6M8 4.2c1.6 2.3 1.6 5.3 0 7.6" fill="none" stroke="#1b5e86" stroke-width=".8"/></svg>
    </div>
    <ul class="contacts">
      <li>0457260714</li>
      <li>08 71526804</li>
      <li>hello@harbourlightmindcarestudio.com.au</li>
      <li>www.harbourlightmindcarestudio.com.au</li>
    </ul>
    <div class="footer-band"></div>
  </section>

  <section class="card card--back" aria-label="Business card back">
    <div class="brand">
      <span class="brand-dot"></span>
      <p class="brand-name">Harbourlight<br>Mindcare Studio</p>
    </div>
  </section>
</main>
</body>
</html>
```